FLYER: Lighting Geometry at Rural Junctions - Review of Signage Placement - training

We are hosting a class in Australia 30, November to 4, December 2020. I would like to have a flyer designed to "sell" the class with description of course topics. I have uploaded a flyer I started on my own but I want it to be professional. Dr. Brenlow only gets to AU every 3-5 years to teach from the US. I would like to have some type of roadway scenery, prefer a nighttime scene.

Target Market(s)

Accident reconstructionists and engineers, police reconstructionists.

Font styles to use
Serif

Colors
fec214

Requirements
Must have
• Name of course and course topics, location of course, price, website and contact information.
Nice to have
• Some type of roadway background, possibly a nighttime scene on a roadway.

```html
<!DOCTYPE html>
<html lang="en">
<head>
<meta charset="utf-8">
<title>Lighting Geometry at Rural Junctions – Training Flyer</title>
<link rel="stylesheet" href="https://fonts.googleapis.com/css2?family=Roboto+Condensed:wght@400;700&family=Arimo:wght@400;700&display=swap">
<style>
  :root {
    --yellow: #fec214;
    --ink: #111111;
    --dark: #262626;
    --white: #ffffff;
    --night-1: #1c1a12;
    --night-2: #6b4a10;
    --night-3: #e39a1c;
  }
  html, body { margin: 0; padding: 0; }
  body {
    width: 1200px; height: 1000px; overflow: hidden;
    background: linear-gradient(#f7f7f7, #e6e6e6);
    font-family: "Arimo", Arial, sans-serif;
    color: var(--ink);
  }
  .flyer {
    position: absolute; left: 240px; top: 18px;
    width: 740px; height: 957px;
    background: var(--white);
    box-shadow: 0 6px 16px rgba(0,0,0,.25);
    overflow: hidden;
  }
  .flyer > * { position: absolute; }
  .backdrop { left: 0; top: 0; width: 740px; height: 957px; }

  .brand { left: 44px; top: 42px; display: flex; align-items: center; gap: 12px; }
  .brand-mark { width: 26px; height: 26px; background: var(--yellow); flex: none; }
  .brand-name {
    font-family: "Roboto Condensed", sans-serif; font-weight: 700;
    font-size: 30px; line-height: 32px; color: var(--ink); letter-spacing: .5px;
  }

  .headline {
    left: 38px; top: 152px; margin: 0;
    font-family: "Roboto Condensed", sans-serif; font-weight: 700;
    font-size: 31px; line-height: 34px; color: var(--ink);
  }
  .headline .accent { color: var(--yellow); text-transform: uppercase; }

  .venue { left: 202px; top: 333px; margin: 0; font-size: 17px; line-height: 23px; color: #222; }

  .presenter-photo {
    left: 0; top: 304px; width: 190px; height: 200px;
    background: linear-gradient(160deg, #c9b8a6 0%, #8e7b6c 45%, #1d1d1d 100%);
  }
  .presenter { left: 203px; top: 415px; color: var(--white); }
  .presenter p { margin: 0; }
  .presenter-role {
    font-family: "Arimo", sans-serif; font-weight: 700;
    font-size: 18px; color: var(--yellow);
  }
  .presenter-title { font-size: 17px; margin: 4px 0 6px !important; }
  .presenter-link { font-size: 9px; font-style: italic; color: #ddd; }

  .topics-heading {
    left: 38px; top: 524px; width: 648px;
    display: flex; align-items: center; gap: 14px;
    font-weight: 700; font-size: 18px; letter-spacing: .5px; margin: 0;
  }
  .topics-heading::before, .topics-heading::after {
    content: ""; flex: 1; height: 3px; background: var(--yellow);
  }
  .topic-list { list-style: none; margin: 0; padding: 0; font-size: 14px; line-height: 17px; }
  .topic-list li { position: relative; padding-left: 25px; margin-bottom: 8px; }
  .topic-list li::before {
    content: "✓"; position: absolute; left: 0; top: 50%; transform: translateY(-50%);
    color: var(--yellow); font-weight: 700; font-size: 19px;
  }
  .topics-left { left: 38px; top: 571px; width: 310px; }
  .topics-right { left: 395px; top: 571px; width: 315px; }
  .topics-left li:last-child { margin-top: 16px; text-align: justify; }
  .column-rule { left: 368px; top: 575px; width: 1px; height: 220px; background: #d5d5d5; }

  .fee { left: 38px; top: 808px; font-weight: 700; font-size: 15px; }

  .footer-band { left: 0; top: 832px; width: 740px; height: 12px; background: var(--yellow); }
  .footer {
    left: 0; top: 844px; width: 740px; height: 113px;
    background: linear-gradient(135deg, #2b2b2b, #1a1a1a);
  }
  .register {
    left: 422px; top: 815px; width: 288px; height: 47px;
    background: var(--yellow); display: flex; align-items: center; justify-content: center;
    font-family: "Arimo", sans-serif; font-weight: 700; font-size: 17px; color: var(--ink);
  }
  .footer-note {
    left: 38px; top: 866px; margin: 0; color: var(--white);
    font-family: "Roboto Condensed", sans-serif; font-weight: 700; font-size: 18px; line-height: 22px;
  }
  .footer-note .accent { color: var(--yellow); }
  .contact {
    right: 52px; top: 872px; text-align: right; color: var(--white); font-size: 16px; line-height: 21px;
  }
  .contact strong { font-weight: 700; }
</style>
</head>
<body>
<article class="flyer">
  <svg class="backdrop" viewBox="0 0 740 957" aria-hidden="true">
    <defs>
      <linearGradient id="nightRoad" x1="0" y1="0" x2="1" y2="1">
        <stop offset="0" stop-color="#6b4a10"/>
        <stop offset=".45" stop-color="#e39a1c"/>
        <stop offset="1" stop-color="#1c1a12"/>
      </linearGradient>
    </defs>
    <rect class="presenter-band" x="0" y="385" width="740" height="119" fill="#272727"/>
    <polygon class="stripe" points="262,0 284,0 740,548 740,580" fill="#fec214"/>
    <polygon class="night-scene" points="284,0 740,0 740,548" fill="url(#nightRoad)" role="img" aria-label="Aerial night view of city highway interchanges lit in orange"/>
  </svg>

  <div class="brand">
    <span class="brand-mark"></span>
    <span class="brand-name">ROADWISE<br>SAFETY GROUP</span>
  </div>

  <h1 class="headline">
    Lighting Geometry<br>
    <span class="accent">at Rural Junctions,</span><br>
    Review of Signage Placement<br>
    OPEN CLASS: &nbsp;CORALBY NSW
  </h1>

  <div class="presenter-photo" role="img" aria-label="Portrait photo of the presenter, Dr. Brenlow"></div>

  <p class="venue">Harbourview Centre – Northpoint Reserve<br>12 Headland Lookout Road, Coralby NSW</p>

  <div class="presenter">
    <p class="presenter-role">PRESENTED BY: DANIEL BRENLOW PH.D.</p>
    <p class="presenter-title">World renowned Human Factors expert</p>
    <span class="presenter-link">Visit www.RoadwiseResearch.com/about/ to learn more about Dr. Brenlow</span>
  </div>

  <h2 class="topics-heading">COURSE TOPICS</h2>

  <ul class="topic-list topics-left">
    <li>Perception-Response Time</li>
    <li>Response to slow moving or stopped<br>vehicles on multilane high speed roads</li>
    <li>Nighttime recognition</li>
    <li>Headlight mapping demonstration and instruction</li>
    <li>Driver decision making</li>
    <li>Gap acceptance for left turns, right turns, and through movements for drivers, riders, and pedestrians</li>
  </ul>
  <div class="column-rule"></div>
  <ul class="topic-list topics-right">
    <li>Research in IDRR</li>
    <li>Pedestrian walking speeds</li>
    <li>Acceleration</li>
    <li>Lateral acceleration (swerving) for cars, motorcycles, and commercial vehicles</li>
    <li>Forward and backward acceleration of cars, motorcycles and commercial vehicles</li>
    <li>Drivers’ responses to green and yellow<br>traffic signals, deceleration choice, reaction time and probability of stopping</li>
  </ul>

  <div class="fee">COURSE FEE: &nbsp;$1,730 AU / $1,200 USD</div>

  <div class="footer-band"></div>
  <div class="footer"></div>
  <div class="register">REGISTER ON OUR WEBSITE</div>

  <p class="footer-note">It has been 3 years since<br>Dr. Brenlow has come to AU to teach,<br><span class="accent">DON’T MISS OUT ON THIS YEAR’S CLASS!</span></p>

  <div class="contact">
    www.roadwisesafety.com<br>
    <strong>or contact us</strong> at 555-014-2286<br>
    Dana@roadwisesafety.com
  </div>
</article>
</body>
</html>
```